Website for IT Security Company in Austria with small and medium business customer base

I own a one man IT security company with a customer small to medium business customer base and need a professional looking website that contains the following information:
- Home page: About the company....
- Services: The services that I offer. It would be nice to have icons if possible (e.g Keystone Ledger icon, digital certificate icon, ...) but this is not a must have.
- About me
- Blog: This is not a must have. It would be ok to just link it to an external blog.
- Impressum
- Contact: No form, just telephone number and e-mail address
- Anything else that you think is necessary for a professional appearance
Also I attached the company design. I do have all source files for the logo if required.

Target Market(s)

Small and medium business of all branches located in Austria

Industry/Entity Type

Cyber Security

Coding

Coded - Design and coding required

Number of Pages Required

5+ page

Font styles to use
Serif
Sans Serif
Other font styles liked:
• Bitsumishi, Bankgothic

Colors

Designer to choose only greyscale colors for use in the design.

Requirements
Must have
• The website must be a mobile-first design.
The design should not be too colorful or playful.
The logo should be used as much as possible
Navigation bar with multi drop-down menu for the services that I offer.
Example:
Services
-> Implementations
-> Implementation Service A
-> Implementation Service B
-> Security Audit
-> Audit A
-> Audit B
Maybe you could have service cards that describe the services briefly and on click redirect to the site that describes the service in detail.
End of example
Logo
contact
impressum
services that I offer
about me
about the company
Nice to have
• Icons would be nice (e.g. house for homepage, letter for contact, ...)
Also for the services I offer icons would be nice (Keystone Ledger, digtial certificates, hacking, security auditing)
For the fonts I have only sugested Bitsumishi and Bankgothic as they are part of my logo. No sure if you feel they make sense as part of the website
Should not have
• forms.
I want to the site to be made as easy as possible (HTML5, CSS, javascript/php/.net)
I do not want a wordpress template or suchlike.

```html
<!DOCTYPE html>
<html lang="en">
<head>
<meta charset="utf-8">
<title>Basalt Guard – Cyber Security &amp; IT Services</title>
<link href="https://fonts.googleapis.com/css2?family=Audiowide&family=Michroma&family=Roboto:wght@400;500&display=swap" rel="stylesheet">
<style>
:root{
  --ink:#000;
  --paper:#fff;
  --text-grey:#6b6b6b;
  --soft-grey:#eeeeee;
  --line-grey:#e4e4e4;
  --accent-blue:#2f6bd8;
  --star:#f4a11b;
}
*{margin:0;padding:0;box-sizing:border-box}
html,body{width:1200px;height:3629px;overflow:hidden;background:var(--paper)}
body{position:relative;font-family:"Michroma",sans-serif;color:var(--ink)}
.abs{position:absolute}
.display{font-family:"Audiowide",sans-serif;text-transform:uppercase;letter-spacing:2px}
.small-caps{font-family:"Michroma",sans-serif;text-transform:uppercase;letter-spacing:.5px}
.btn{position:absolute;display:flex;align-items:center;justify-content:center;font-family:"Michroma",sans-serif;text-transform:uppercase;letter-spacing:2px;font-size:12px;text-decoration:none;clip-path:polygon(9% 0,91% 0,100% 50%,91% 100%,9% 100%,0 50%);filter:drop-shadow(3px 4px 3px rgba(0,0,0,.35))}
.btn-dark{background:var(--ink);color:var(--paper)}
.btn-light{background:var(--paper);color:var(--ink)}

/* nav */
.site-nav{left:0;top:0;width:1200px;height:53px;background:var(--ink)}
.brand{left:94px;top:16px;display:flex;align-items:center;gap:10px;color:var(--paper);font-family:"Audiowide",sans-serif;font-size:18px;letter-spacing:2px;text-transform:uppercase}
.brand-dot{width:22px;height:22px;border-radius:50%;background:var(--paper)}
.nav-link{top:22px;color:var(--paper);font-size:8.5px;letter-spacing:1.5px;text-transform:uppercase;text-decoration:none}

/* hero */
.hero-title{left:92px;top:150px;font-size:38px;line-height:54px;letter-spacing:4px}
.hero-text{left:94px;top:280px;width:410px;font-size:9.5px;line-height:20px;letter-spacing:.5px}
.hero-art{left:730px;top:120px;width:360px;height:345px;border-radius:44% 44% 10% 10%;background:radial-gradient(circle at 55% 50%,#3b2f4a 0,#1a1420 55%,#f0f0f0 56%,#f7f7f7 100%)}

/* about company */
.about-co{left:0;top:563px;width:1200px;height:417px}
.about-co-panel{left:0;top:0;width:1200px;height:417px;background:var(--ink);clip-path:polygon(430px 0,1200px 0,1200px 417px,430px 417px,549px 207px)}
.about-co-art{left:56px;top:0;width:493px;height:417px;background:linear-gradient(135deg,#0d1f4a,#2b5fb8 50%,#0b1a3c);clip-path:polygon(127px 0,374px 0,493px 207px,374px 417px,127px 417px,0 207px)}
.section-title-light{color:var(--paper);font-size:24px}
.body-light{color:var(--paper);font-size:8.5px;line-height:22px;letter-spacing:.6px;text-transform:uppercase}

/* services */
.svc-title{left:104px;top:1112px;font-size:24px;line-height:34px}
.svc-text{left:106px;top:1196px;width:320px;font-size:8px;line-height:15px;color:var(--text-grey)}
.svc-card{top:1088px;width:307px;height:244px;color:var(--paper);text-align:center}
.svc-card .shade{position:absolute;inset:0}
.svc-card h3{position:absolute;top:68px;left:0;width:100%;font-family:"Audiowide",sans-serif;font-size:16px;letter-spacing:1.5px;text-transform:uppercase;font-weight:400}
.svc-card p{position:absolute;top:118px;left:28px;right:28px;font-size:9px;line-height:16px;letter-spacing:.8px;text-transform:uppercase}

/* about me */
.about-me{left:0;top:1426px;width:1200px;height:416px;background:var(--ink)}
.about-me-art{left:641px;top:1404px;width:500px;height:438px;background:linear-gradient(180deg,#f2f2f2 0,#d6d6d6 40%,#2d3035 41%,#14161a 100%);clip-path:polygon(120px 0,380px 0,500px 230px,400px 438px,100px 438px,0 230px)}

/* testimonials */
.center-title{left:0;width:1200px;text-align:center;font-size:24px}
.center-sub{left:0;width:1200px;text-align:center;font-size:8.5px;line-height:17px;color:var(--text-grey);letter-spacing:.8px;text-transform:uppercase}
.quote{top:2078px;width:240px;text-align:center}
.quote-bg{position:absolute;left:68px;top:26px;width:104px;height:58px;background:var(--soft-grey);border-radius:6px}
.avatar{position:relative;margin:0 auto;width:46px;height:46px;border-radius:50%;background:linear-gradient(180deg,#c7cbd1,#3a3f4a)}
.quote-name{position:relative;margin-top:20px;font-family:"Audiowide",sans-serif;font-size:10px;letter-spacing:1px;text-transform:uppercase}
.stars{position:relative;margin-top:6px;color:var(--star);font-size:13px;letter-spacing:6px}
.quote-text{position:relative;margin-top:6px;font-size:8.5px;line-height:16px;color:var(--text-grey);letter-spacing:.8px;text-transform:uppercase}
.arrow-btn{top:2145px;width:26px;height:26px}

/* problem band */
.problem{left:0;top:2384px;width:1200px;height:291px;background:var(--ink)}

/* news */
.news-card{top:2912px;width:276px;height:324px;border:1px solid var(--line-grey);background:var(--paper)}
.news-img{position:absolute;left:0;top:0;width:276px;height:166px}
.news-meta{position:absolute;left:6px;top:184px;font-size:7px;color:var(--text-grey);letter-spacing:.5px;text-transform:uppercase}
.news-title{position:absolute;left:6px;top:202px;font-family:"Audiowide",sans-serif;font-size:11.5px;letter-spacing:1.5px;text-transform:uppercase}
.news-text{position:absolute;left:6px;top:224px;width:256px;font-size:7.8px;line-height:16px;color:var(--text-grey);letter-spacing:.6px;text-transform:uppercase}
.news-foot{position:absolute;left:6px;right:14px;top:302px;display:flex;justify-content:space-between;font-size:7px;text-transform:uppercase;color:var(--text-grey)}
.news-foot a{color:var(--accent-blue);text-decoration:none;font-family:"Audiowide",sans-serif}

/* footer */
.site-footer{left:0;top:3341px;width:1200px;height:288px;background:var(--ink);color:var(--paper);font-family:"Roboto",sans-serif}
.foot-link{position:absolute;font-size:13px;color:var(--paper);text-decoration:none}
.foot-head{position:absolute;font-size:18px;font-weight:400}
.foot-info{position:absolute;font-size:12.5px;line-height:16px}
.social{position:absolute;top:116px;font-size:10px;display:flex;align-items:center;gap:4px}
.social i{display:inline-block;width:8px;height:8px;background:var(--paper)}
.copyright{position:absolute;left:0;top:236px;width:1200px;text-align:center;font-size:10px}
</style>
</head>
<body>

<header class="abs site-nav">
  <div class="abs brand"><span class="brand-dot"></span>Basalt Guard</div>
  <a class="abs nav-link" style="left:589px" href="#">Home</a>
  <a class="abs nav-link" style="left:662px" href="#">Service</a>
  <a class="abs nav-link" style="left:748px" href="#">About me</a>
  <a class="abs nav-link" style="left:849px" href="#">Blog</a>
  <a class="abs nav-link" style="left:917px" href="#">Impressum</a>
  <a class="abs nav-link" style="left:1020px" href="#">Contact us</a>
</header>

<section class="hero">
  <h1 class="abs display hero-title">Cyber Sercurity<br>&amp; IT Services</h1>
  <p class="abs hero-text">IT Security Is A Set Of Cybersecurity Strategies That Prevents Unauthorized Access To Organizational Assets Such As Computers, Networks, And Data.</p>
  <a class="btn btn-dark" style="left:94px;top:394px;width:183px;height:46px" href="#">Get Started</a>
  <div class="abs hero-art" role="img" aria-label="Illustration of a person with a laptop on a dark cloud beside a shield with a padlock and gears"></div>
</section>

<section class="abs about-co">
  <div class="abs about-co-art" role="img" aria-label="Blue digital network of hexagons with padlocks and binary code"></div>
  <div class="abs about-co-panel"></div>
  <h2 class="abs display section-title-light" style="left:600px;top:88px">About Basalt Guard</h2>
  <p class="abs body-light" style="left:600px;top:143px;width:440px">Lorem ipsum dolor sit amet, consectetur adipiscing elit. Tortor quis elit pellentesque ultrices non ultricies diam tincidunt bibendum. Quam et sit mauris tincidunt mi mattis congue. Aenean faucibus mollis orci arcu. Sit libero nibh nisl mattis phasellus bibendum purus tellus quis.</p>
  <a class="btn btn-light" style="left:603px;top:307px;width:162px;height:35px;font-size:10px" href="#">Learn More</a>
</section>

<section class="services">
  <h2 class="abs display svc-title">Service We<br>Offer</h2>
  <p class="abs svc-text small-caps">Lorem ipsum dolor sit amet, consectetur adipiscing elit ut aliquam, purus sit amet luctus venenatis, lectus magna</p>
  <a class="btn btn-dark" style="left:106px;top:1270px;width:183px;height:45px" href="#">Learn More</a>
  <a class="abs svc-card" style="left:458px" href="#">
    <div class="shade" role="img" aria-label="Dark photo of hands with an open book" style="background:linear-gradient(160deg,#2a2a2a,#4a4640 60%,#1c1c1c)"></div>
    <h3>Implementations</h3>
    <p>Lorem ipsum dolor sit amet, consectetur adipiscing elit ut aliquam, purus sit amet luctus</p>
  </a>
  <a class="abs svc-card" style="left:791px" href="#">
    <div class="shade" role="img" aria-label="Dark photo of hands typing on a laptop" style="background:linear-gradient(160deg,#1f1f1f,#4b4b4b 60%,#232323)"></div>
    <h3>Security Audit</h3>
    <p>Lorem ipsum dolor sit amet, consectetur adipiscing elit ut aliquam, purus sit amet luctus</p>
  </a>
</section>

<section>
  <div class="abs about-me"></div>
  <div class="abs about-me-art" role="img" aria-label="Photo of a smiling businessman in a dark suit with arms crossed"></div>
  <h2 class="abs display section-title-light" style="left:104px;top:1518px">About Me</h2>
  <p class="abs body-light" style="left:105px;top:1570px;width:440px">Lorem ipsum dolor sit amet, consectetur adipiscing elit. Tortor quis elit pellentesque ultrices non ultricies diam tincidunt bibendum. Quam et sit mauris tincidunt mi mattis congue. Aenean faucibus mollis orci arcu. Sit libero nibh nisl mattis phasellus bibendum purus tellus quis.</p>
  <a class="btn btn-light" style="left:108px;top:1736px;width:162px;height:35px;font-size:10px" href="#">Learn More</a>
</section>

<section class="testimonials">
  <h2 class="abs display center-title" style="top:1942px">Testimonial</h2>
  <p class="abs center-sub" style="top:1990px">Lorem ipsum dolor sit amet, consectetur adipiscing elit ut<br>aliquam, purus sit amet luctus venenatis, lectus magna</p>
  <svg class="abs arrow-btn" style="left:105px" viewBox="0 0 26 26" aria-label="Previous"><circle cx="13" cy="13" r="12" fill="#555"/><path d="M19 13H8M12 8l-5 5 5 5" stroke="#fff" stroke-width="2.4" fill="none"/></svg>
  <svg class="abs arrow-btn" style="left:1055px" viewBox="0 0 26 26" aria-label="Next"><circle cx="13" cy="13" r="12" fill="#555"/><path d="M7 13h11M14 8l5 5-5 5" stroke="#fff" stroke-width="2.4" fill="none"/></svg>
  <div class="abs quote" style="left:178px">
    <div class="quote-bg"></div>
    <div class="avatar" role="img" aria-label="Portrait photo of the reviewer"></div>
    <div class="quote-name">Marlon Avery</div>
    <div class="stars">★★★★★</div>
    <p class="quote-text">Lorem ipsum dolor sit amet, consectetur adipiscing elit ut aliquam, purus sit amet luctus venenatis, lectus magna purus sit amet luctus venenatis.</p>
  </div>
  <div class="abs quote" style="left:471px">
    <div class="quote-bg"></div>
    <div class="avatar" role="img" aria-label="Portrait photo of the reviewer"></div>
    <div class="quote-name">Marlon Avery</div>
    <div class="stars">★★★★★</div>
    <p class="quote-text">Lorem ipsum dolor sit amet, consectetur adipiscing elit ut aliquam, purus sit amet luctus venenatis, lectus magna purus sit amet luctus venenatis.</p>
  </div>
  <div class="abs quote" style="left:764px">
    <div class="quote-bg"></div>
    <div class="avatar" role="img" aria-label="Portrait photo of the reviewer"></div>
    <div class="quote-name">Marlon Avery</div>
    <div class="stars">★★★★★</div>
    <p class="quote-text">Lorem ipsum dolor sit amet, consectetur adipiscing elit ut aliquam, purus sit amet luctus venenatis, lectus magna purus sit amet luctus venenatis.</p>
  </div>
</section>

<section class="abs problem">
  <h2 class="abs display center-title" style="top:60px;color:var(--paper)">Have Any Problem?</h2>
  <p class="abs center-sub" style="top:114px;color:var(--paper);font-size:9px;line-height:22px;letter-spacing:1px">Lorem ipsum dolor sit amet, consectetur adipiscing elit. Tortor quis elit<br>pellentesque ultrices non ultricies diam tincidunt bibendum.</p>
  <a class="btn btn-light" style="left:521px;top:190px;width:160px;height:39px;font-size:10px" href="#">Get Started</a>
</section>

<section class="news">
  <h2 class="abs display center-title" style="top:2776px">Latest News</h2>
  <p class="abs center-sub" style="top:2818px">Lorem ipsum dolor sit amet, consectetur adipiscing elit ut<br>aliquam, purus sit amet luctus venenatis, lectus magna</p>
  <article class="abs news-card" style="left:131px">
    <div class="news-img" role="img" aria-label="Photo of a circuit board, a coffee cup and a laptop keyboard" style="background:linear-gradient(135deg,#1c2a3a,#5b6e84 55%,#2b3038)"></div>
    <div class="news-meta">Data handling · 1 Month Ago</div>
    <h3 class="news-title">Data Analysis</h3>
    <p class="news-text">Lorem ipsum dolor sit amet, consectetur adipiscing elit ut aliquam, purus sit amet luctus venenatis, lectus magna.</p>
    <div class="news-foot"><span>1 Month Ago</span><a href="#">Read Full →</a></div>
  </article>
  <article class="abs news-card" style="left:462px">
    <div class="news-img" role="img" aria-label="Grey graphic of a fingerprint and security icons in hexagons" style="background:linear-gradient(135deg,#2a2a2a,#8a8a8a 55%,#3a3a3a)"></div>
    <div class="news-meta">Security · 1 Month Ago</div>
    <h3 class="news-title">Cyber Hacks</h3>
    <p class="news-text">Lorem ipsum dolor sit amet, consectetur adipiscing elit ut aliquam, purus sit amet luctus venenatis, lectus magna.</p>
    <div class="news-foot"><span>1 Month Ago</span><a href="#">Read Full →</a></div>
  </article>
  <article class="abs news-card" style="left:793px">
    <div class="news-img" role="img" aria-label="Hooded figure in front of glowing cyan code" style="background:linear-gradient(180deg,#1bb7d6,#0b4d6b 55%,#06222f)"></div>
    <div class="news-meta">Front-end · 1 Month Ago</div>
    <h3 class="news-title">Cyber Hacks</h3>
    <p class="news-text">Lorem ipsum dolor sit amet, consectetur adipiscing elit ut aliquam, purus sit amet luctus venenatis, lectus magna.</p>
    <div class="news-foot"><span>1 Month Ago</span><a href="#">Read Full →</a></div>
  </article>
</section>

<footer class="abs site-footer">
  <a class="foot-link" style="left:113px;top:66px" href="#">Core main</a>
  <a class="foot-link" style="left:113px;top:98px" href="#">Entry advance</a>
  <a class="foot-link" style="left:113px;top:130px" href="#">Bank exams</a>
  <a class="foot-link" style="left:113px;top:163px" href="#">Civic board</a>
  <a class="foot-link" style="left:113px;top:195px" href="#">Staff exams</a>
  <a class="foot-link" style="left:318px;top:66px" href="#">About</a>
  <a class="foot-link" style="left:318px;top:98px" href="#">Career</a>
  <a class="foot-link" style="left:318px;top:130px" href="#">Privacy policy</a>
  <a class="foot-link" style="left:318px;top:163px" href="#">Blogs</a>
  <a class="foot-link" style="left:318px;top:195px" href="#">Contacts</a>
  <h4 class="foot-head" style="left:529px;top:66px">Contact us</h4>
  <svg class="abs" style="left:531px;top:116px" width="18" height="14" viewBox="0 0 18 14" aria-hidden="true"><rect x="1" y="1" width="16" height="12" fill="none" stroke="#fff" stroke-width="1.5"/><path d="M1 1l8 7 8-7" fill="none" stroke="#fff" stroke-width="1.5"/></svg>
  <div class="foot-info" style="left:561px;top:115px">elsa.brandt@example.com</div>
  <svg class="abs" style="left:532px;top:153px" width="14" height="18" viewBox="0 0 14 18" aria-hidden="true"><path d="M7 17S1 10 1 6.5a6 6 0 0 1 12 0C13 10 7 17 7 17z" fill="none" stroke="#fff" stroke-width="1.5"/><circle cx="7" cy="6.5" r="2" fill="none" stroke="#fff" stroke-width="1.5"/></svg>
  <div class="foot-info" style="left:561px;top:153px">412 Harrow Lane, Fenwick,<br>Ontario 20417 Canada</div>
  <h4 class="foot-head" style="left:862px;top:66px">Follow us</h4>
  <span class="social" style="left:862px"><i></i>Loop</span>
  <span class="social" style="left:905px"><i></i>Chirp</span>
  <span class="social" style="left:950px"><i></i>Snap</span>
  <span class="social" style="left:995px"><i></i>Reel</span>
  <div class="copyright">COPYRIGHT 2020</div>
</footer>

</body>
</html>
```